Bramble Roofing Website Relaunch

We require a re-launch of our website, We are a longrun roofing company based in New Zealand, we are rapidly expanding and require a more professionally presented website our current website is www.brambleroofing.co.nz we want something modern, masculine and communicates a "strong" "superior" image, we already have a logo which I have attached we use the orange and silver one as you will see on our current website

Industry/Entity Type

It Company

Number of Pages Required

1 page

Colors
f37122
f78f20
000000
1b1b1b
474747
d3d3d3
f5f5f5

Requirements
Must have
• Images of our work
• Email and Mobile Contact Details
• Link to Facebook page
• Who We Are, What We Do
• Certified Trade Craftsman Logo
• Our Logo

```html
<!DOCTYPE html>
<html lang="en">
<head>
<meta charset="utf-8">
<title>Bramble Roofing</title>
<link href="https://fonts.googleapis.com/css2?family=Exo:wght@600;700&family=Lato:wght@400;700&family=Oswald:wght@400&display=swap" rel="stylesheet">
<style>
:root{
  --orange:#f37122;
  --orange-light:#f78f20;
  --orange-deep:#c4622a;
  --black:#000000;
  --ink:#1b1b1b;
  --charcoal:#333333;
  --dark:#474747;
  --silver:#d3d3d3;
  --mist:#f5f5f5;
  --grey-panel:#8a8a8a;
  --grey-title:#6e6e6e;
  --section-grey:#eeeeee;
  --white:#ffffff;
}
*{box-sizing:border-box;margin:0;padding:0}
html,body{width:1200px;height:2575px;overflow:hidden;background:var(--white)}
body{font-family:"Lato",sans-serif;color:var(--dark);position:relative}

/* Header */
.site-header{position:absolute;top:0;left:0;width:1200px;height:127px;border-bottom:3px solid var(--orange);background:var(--white)}
.brand{position:absolute;left:100px;top:30px;display:flex;align-items:center;gap:14px}
.brand-mark{width:44px;height:44px;background:var(--orange)}
.brand-name{font-family:"Exo",sans-serif;font-weight:700;font-size:30px;color:var(--orange);line-height:1}
.contact-bar{position:absolute;right:98px;top:16px;display:flex;align-items:center;gap:14px;font-size:16px;color:#777}
.contact-item{display:flex;align-items:center;gap:12px}
.diamond-icon{width:38px;height:38px;display:block}
.main-nav{position:absolute;right:100px;top:80px;display:flex;gap:40px;font-family:"Exo",sans-serif;font-weight:700;font-size:16px;color:#666;letter-spacing:.3px}
.main-nav .active{color:var(--orange)}

/* Hero */
.hero{position:absolute;top:127px;left:0;width:1200px;height:513px;background:linear-gradient(100deg,#d9b77e 0%,#c89c5e 30%,#5e5e5e 45%,#3f4244 75%,#55585a 100%)}
.hero-caption{position:absolute;left:0;right:0;bottom:20px;text-align:center;font-family:"Oswald",sans-serif;font-size:35px;color:var(--white);letter-spacing:.5px}
.hero-arrow{position:absolute;top:218px;width:36px;height:34px;background:var(--ink);display:flex;align-items:center;justify-content:center}
.hero-arrow.prev{left:6px}.hero-arrow.next{right:6px}

/* Service highlights */
.highlights{position:absolute;top:640px;left:0;width:1200px;height:135px;display:flex}
.highlight{width:600px;height:135px;display:flex;align-items:flex-start;padding:20px 0 0 96px;gap:38px;color:var(--white)}
.highlight.residential{background:var(--grey-panel)}
.highlight.commercial{background:linear-gradient(180deg,var(--orange-deep),var(--orange-light))}
.highlight-icon{width:108px;height:108px;flex:none;margin-top:-6px}
.highlight h3{font-family:"Exo",sans-serif;font-weight:700;font-size:19px;letter-spacing:.5px;margin:4px 0 6px}
.highlight p{font-size:14px;line-height:21px;width:330px}

/* Section headings */
.section-title{text-align:center;font-family:"Exo",sans-serif;font-weight:700;font-size:31px;color:var(--grey-title);letter-spacing:.3px}
.section-title span{color:var(--orange)}
.divider{display:block;margin:10px auto 0;width:120px;height:24px}

.who-we-are{position:absolute;top:775px;left:0;width:1200px;height:313px;padding-top:42px}
.who-we-are p{width:1060px;margin:20px auto 0;text-align:center;font-size:14px;line-height:27px;color:#444}
.btn{display:block;margin:20px auto 0;width:122px;height:37px;background:linear-gradient(180deg,var(--orange),var(--orange-deep));color:var(--white);font-family:"Exo",sans-serif;font-weight:700;font-size:13px;text-align:center;line-height:37px;border-bottom:2px solid #a9521f}

/* What we do */
.what-we-do{position:absolute;top:1088px;left:0;width:1200px;height:750px;background:var(--section-grey);padding-top:42px}
.what-we-do .intro{text-align:center;font-size:14px;color:#444;margin-top:24px}
.service-grid{position:absolute;top:192px;left:100px;width:1000px;display:grid;grid-template-columns:repeat(3,314px);column-gap:29px;row-gap:40px}
.service-card{height:233px;border:4px solid #7d7d7d;background:#7d7d7d;display:flex;flex-direction:column}
.service-photo{flex:1}
.service-label{height:45px;background:linear-gradient(180deg,var(--orange-light),var(--orange-deep));color:var(--white);font-family:"Exo",sans-serif;font-weight:700;font-size:16px;text-align:center;line-height:45px;letter-spacing:.4px}

/* Our work */
.our-work{position:absolute;top:1838px;left:0;width:1200px;height:407px;padding-top:42px}
.gallery{position:absolute;top:140px;left:0;width:1200px;height:159px;display:flex;gap:2px}
.gallery-item{flex:1;position:relative}
.gallery-item.featured{background:rgba(40,40,40,.88);color:var(--white);text-align:center;font-size:14px;line-height:20px;padding-top:38px}
.gallery-plus{display:block;margin:0 auto 10px;width:30px;height:30px}
.gallery-rule{position:absolute;top:341px;left:0;width:1200px;height:1px;background:#bbb}
.gallery-nav{position:absolute;top:329px;left:578px;display:flex;gap:6px}
.gallery-dot{width:26px;height:26px;border-radius:50%;background:#cfcfcf;display:flex;align-items:center;justify-content:center}
.gallery-dot.on{background:#3a3a3a}

/* Footer */
.site-footer{position:absolute;top:2245px;left:0;width:1200px;height:285px;background:var(--charcoal);color:var(--white)}
.footer-col{position:absolute;top:48px}
.footer-col h4{font-family:"Exo",sans-serif;font-weight:700;font-size:15px;letter-spacing:.5px;margin-bottom:22px}
.quick-links{left:100px}
.quick-links li{list-style:none;font-size:12px;margin-bottom:16px;display:flex;align-items:center;gap:10px}
.contact-details{left:305px}
.contact-row{display:flex;gap:14px;font-size:12px;margin-bottom:18px;line-height:18px}
.contact-row svg{flex:none;width:14px;height:16px;margin-top:1px}
.contact-row strong{font-weight:700}
.inquiry{left:632px;width:245px}
.field{height:30px;border:1px solid #9a9a9a;margin-bottom:9px;font-size:11px;padding-left:8px;line-height:28px}
.submit{width:82px;height:30px;background:var(--orange);font-family:"Exo",sans-serif;font-weight:700;font-size:12px;text-align:center;line-height:30px;margin-top:2px}
.badge{position:absolute;left:970px;top:90px;width:132px;height:132px;background:var(--white);border-radius:4px}
.badge-shape{position:absolute;left:12px;top:12px;width:108px;height:108px;border-radius:50%;border:6px solid #222}

.bottom-bar{position:absolute;top:2530px;left:0;width:1200px;height:45px;background:linear-gradient(180deg,var(--orange-deep),var(--orange-light));color:var(--white);font-size:12px}
.bottom-bar p{position:absolute;left:100px;top:14px}
.bottom-bar .social{position:absolute;right:98px;top:6px}
</style>
</head>
<body>

<header class="site-header">
  <div class="brand">
    <span class="brand-mark"></span>
    <span class="brand-name">Bramble Roofing</span>
  </div>
  <div class="contact-bar">
    <div class="contact-item">
      <svg class="diamond-icon" viewBox="0 0 38 38"><rect x="7" y="7" width="24" height="24" transform="rotate(45 19 19)" fill="none" stroke="#999" stroke-width="1.5"/><path d="M14 13c1-1 2-1 3 1l1 2c0 1-1 1-1 2 1 2 2 3 4 4 1 0 1-1 2-1l2 1c2 1 2 2 1 3-2 2-5 1-8-2s-4-7-4-10z" fill="var(--orange)"/></svg>
      <span>021 555 01234</span>
    </div>
    <div class="contact-item">
      <svg class="diamond-icon" viewBox="0 0 38 38"><rect x="7" y="7" width="24" height="24" transform="rotate(45 19 19)" fill="none" stroke="#999" stroke-width="1.5"/><rect x="12" y="14" width="14" height="10" fill="var(--orange)"/><path d="M12 14l7 5 7-5" fill="none" stroke="#fff" stroke-width="1.2"/></svg>
      <span>hello@brambleroofing.co.nz</span>
    </div>
    <svg class="diamond-icon" viewBox="0 0 38 38" role="img" aria-label="Social page link"><rect x="7" y="7" width="24" height="24" transform="rotate(45 19 19)" fill="none" stroke="#999" stroke-width="1.5"/></svg>
  </div>
  <nav class="main-nav">
    <span class="active">HOME</span><span>WHO WE ARE</span><span>WHAT WE DO</span><span>OUR WORK</span><span>CONTACT US</span>
  </nav>
</header>

<section class="hero" role="img" aria-label="Roofer in a safety harness laying dark roof sheets over timber framing">
  <span class="hero-arrow prev"><svg width="12" height="16" viewBox="0 0 12 16"><path d="M9 2L3 8l6 6" fill="none" stroke="#fff" stroke-width="2.5"/></svg></span>
  <span class="hero-arrow next"><svg width="12" height="16" viewBox="0 0 12 16"><path d="M3 2l6 6-6 6" fill="none" stroke="#fff" stroke-width="2.5"/></svg></span>
  <div class="hero-caption">LONG RUN ROOFING SPECIALISTS</div>
</section>

<section class="highlights">
  <div class="highlight residential">
    <svg class="highlight-icon" viewBox="0 0 108 108"><rect x="22" y="22" width="64" height="64" transform="rotate(45 54 54)" fill="none" stroke="#fff" stroke-width="5"/><path d="M38 55l16-14 16 14v14H38z" fill="#fff"/><rect x="50" y="59" width="8" height="10" fill="var(--grey-panel)"/></svg>
    <div><h3>RESIDENTIAL</h3><p>Lorem ipsum dolor sit amet, consectetuer adipiscing elit, sed diam nonummy nibh euismod tincidunt ut laoreet dolore magna aliquam erat...[+]</p></div>
  </div>
  <div class="highlight commercial">
    <svg class="highlight-icon" viewBox="0 0 108 108"><rect x="22" y="22" width="64" height="64" transform="rotate(45 54 54)" fill="none" stroke="#fff" stroke-width="5"/><rect x="42" y="38" width="24" height="32" fill="#fff"/><g fill="var(--orange-deep)"><rect x="46" y="42" width="4" height="4"/><rect x="52" y="42" width="4" height="4"/><rect x="58" y="42" width="4" height="4"/><rect x="46" y="50" width="4" height="4"/><rect x="52" y="50" width="4" height="4"/><rect x="58" y="50" width="4" height="4"/><rect x="51" y="60" width="6" height="10"/></g></svg>
    <div><h3>COMMERCIAL</h3><p>Lorem ipsum dolor sit amet, consectetuer adipiscing elit, sed diam nonummy nibh euismod tincidunt ut laoreet dolore magna aliquam erat...[+]</p></div>
  </div>
</section>

<section class="who-we-are">
  <h2 class="section-title">WHO <span>WE ARE</span></h2>
  <svg class="divider" viewBox="0 0 120 24"><line x1="0" y1="12" x2="48" y2="12" stroke="#bbb"/><line x1="72" y1="12" x2="120" y2="12" stroke="#bbb"/><rect x="53" y="5" width="14" height="14" transform="rotate(45 60 12)" fill="none" stroke="#999"/><rect x="57" y="9" width="6" height="6" fill="var(--orange)"/></svg>
  <p>We are a local, family owned and operated company with over 18 years extensive experience in the roofing industry, Roofing not only Waikato and Auckland but surrounding areas also. We are committed to providing superior service to our customers regardless of how big or small your project is, Your satisfaction is our guarantee. We take pride in installing quality products, Offering a workmanship guarantee and manufacturers material warranties where applicable.</p>
  <span class="btn">READ MORE</span>
</section>

<section class="what-we-do">
  <h2 class="section-title">WHAT <span>WE DO</span></h2>
  <svg class="divider" viewBox="0 0 120 24"><line x1="0" y1="12" x2="48" y2="12" stroke="#bbb"/><line x1="72" y1="12" x2="120" y2="12" stroke="#bbb"/><rect x="53" y="5" width="14" height="14" transform="rotate(45 60 12)" fill="none" stroke="#999"/><rect x="57" y="9" width="6" height="6" fill="var(--orange)"/></svg>
  <p class="intro">At Bramble Roofing we offer a variety of professional services specializing in Residential, Industrial and Commercial Long Run Roofing Installations</p>
  <div class="service-grid">
    <div class="service-card"><div class="service-photo" role="img" aria-label="House with a new roof and scaffolding" style="background:linear-gradient(180deg,#9fb6c9,#7e8c8a 55%,#6f7a4f)"></div><div class="service-label">New Roofs And Re-Roofs</div></div>
    <div class="service-card"><div class="service-photo" role="img" aria-label="Dark metal cladding on a house exterior" style="background:linear-gradient(180deg,#cfd3d4,#3a3b3c 40%,#5a5d58)"></div><div class="service-label">Metal Cladding</div></div>
    <div class="service-card"><div class="service-photo" role="img" aria-label="Building with dark spouting and metal fascia" style="background:linear-gradient(180deg,#b7c4ce,#2f3132 45%,#7b7a70)"></div><div class="service-label">Spouting and Metal Fascia</div></div>
    <div class="service-card"><div class="service-photo" role="img" aria-label="Large shed with down pipes" style="background:linear-gradient(180deg,#c9d4dc,#55605a 45%,#6c5a48)"></div><div class="service-label">Down Pipes</div></div>
    <div class="service-card"><div class="service-photo" role="img" aria-label="Building alteration under construction" style="background:linear-gradient(180deg,#d6dde3,#4e5558 45%,#3f4442)"></div><div class="service-label">Alterations</div></div>
    <div class="service-card"><div class="service-photo" role="img" aria-label="Dark roof extension seen from above" style="background:linear-gradient(135deg,#6c8a5a,#2a2d30 35%,#50565a)"></div><div class="service-label">Extensions</div></div>
  </div>
</section>

<section class="our-work">
  <h2 class="section-title">OUR <span>WORK</span></h2>
  <svg class="divider" viewBox="0 0 120 24"><line x1="0" y1="12" x2="48" y2="12" stroke="#bbb"/><line x1="72" y1="12" x2="120" y2="12" stroke="#bbb"/><rect x="53" y="5" width="14" height="14" transform="rotate(45 60 12)" fill="none" stroke="#999"/><rect x="57" y="9" width="6" height="6" fill="var(--orange)"/></svg>
  <div class="gallery">
    <div class="gallery-item" role="img" aria-label="Large house with a new dark roof" style="background:linear-gradient(180deg,#aebccb,#4d5154 60%,#7a7772)"></div>
    <div class="gallery-item" role="img" aria-label="Wide commercial roof at dusk" style="background:linear-gradient(180deg,#8f9aa4,#c5c9cc 55%,#5c6548)"></div>
    <div class="gallery-item featured" style="background:linear-gradient(rgba(40,40,40,.85),rgba(40,40,40,.85)),#6d7479">
      <svg class="gallery-plus" viewBox="0 0 30 30"><circle cx="15" cy="15" r="13" fill="none" stroke="#fff" stroke-width="1.5"/><path d="M15 9v12M9 15h12" stroke="#fff" stroke-width="1.5"/></svg>
      Lorem ipsum dolor sit amet,<br>consectetuer adipiscing .
    </div>
    <div class="gallery-item" role="img" aria-label="Metal roof ridge viewed from the top" style="background:linear-gradient(180deg,#a8b1b9,#4b5055 45%,#3b3e41)"></div>
    <div class="gallery-item" role="img" aria-label="Villa with a freshly installed roof" style="background:linear-gradient(180deg,#c3cdd6,#727b80 50%,#5c6a45)"></div>
  </div>
  <div class="gallery-rule"></div>
  <div class="gallery-nav">
    <span class="gallery-dot"><svg width="10" height="12" viewBox="0 0 10 12"><path d="M7 1L2 6l5 5" fill="none" stroke="#fff" stroke-width="2"/></svg></span>
    <span class="gallery-dot on"><svg width="10" height="12" viewBox="0 0 10 12"><path d="M3 1l5 5-5 5" fill="none" stroke="#fff" stroke-width="2"/></svg></span>
  </div>
</section>

<footer class="site-footer">
  <div class="footer-col quick-links">
    <h4>QUICK LINKS</h4>
    <ul>
      <li><span>›</span>Home</li><li><span>›</span>Who We Are</li><li><span>›</span>What We Do</li><li><span>›</span>Our Work</li><li><span>›</span>Contact Us</li>
    </ul>
  </div>
  <div class="footer-col contact-details">
    <h4>CONTACT DETAILS</h4>
    <div class="contact-row"><svg viewBox="0 0 14 16"><path d="M7 1a5 5 0 0 1 5 5c0 4-5 9-5 9S2 10 2 6a5 5 0 0 1 5-5z" fill="#fff"/><circle cx="7" cy="6" r="2" fill="var(--charcoal)"/></svg><div><strong>Bramble Roofing Ltd</strong><br>Riverside, Ashgrove, New Zealand</div></div>
    <div class="contact-row"><svg viewBox="0 0 14 16"><path d="M2 3c1-1 2-1 3 1l1 2c0 1-1 1-1 2 1 2 2 3 3 4 1 0 1-1 2-1l2 1c1 1 1 2 0 3-2 1-5 0-7-2S1 5 2 3z" fill="#fff"/></svg><div>021 555 01234</div></div>
    <div class="contact-row"><svg viewBox="0 0 14 16"><rect x="1" y="7" width="12" height="7" fill="#fff"/><rect x="3" y="3" width="8" height="4" fill="none" stroke="#fff"/></svg><div>021 555 01234</div></div>
    <div class="contact-row"><svg viewBox="0 0 14 16"><rect x="1" y="4" width="12" height="9" fill="#fff"/><path d="M1 4l6 5 6-5" fill="none" stroke="var(--charcoal)"/></svg><div>hello@brambleroofing.co.nz</div></div>
  </div>
  <div class="footer-col inquiry">
    <h4>QUICK INQUIRY</h4>
    <div class="field">Name</div>
    <div class="field">Email</div>
    <div class="field">Message</div>
    <div class="submit">SUBMIT</div>
  </div>
  <div class="badge" role="img" aria-label="Certified Trade Craftsman badge"><span class="badge-shape"></span></div>
</footer>

<div class="bottom-bar">
  <p>Copyright © 2017 <strong>Bramble Roofing</strong>. All Rights Reserved</p>
  <svg class="social" width="34" height="34" viewBox="0 0 34 34" role="img" aria-label="Social page link"><rect x="7" y="7" width="20" height="20" transform="rotate(45 17 17)" fill="none" stroke="#fff" stroke-width="1.5"/></svg>
</div>

</body>
</html>
```